Branding website for a Data Science company with 1 product

Branding website for a Data Science company, featuring our main product: Lumoria. The purpose of the website is to get potential clients to get a peek at what we do, but the main purpose is to get them to get in touch with us. The website will not answer all questions. Therefore the contact details and contact form is a must-have .

Target Market(s)

Potential new B2B clients with medium to large websites, application users (behind a login)

Industry/Entity Type

It Company

Coding

Coded - Design and coding required

Number of Pages Required

2 page

Font styles to use
Sans Serif

Colors

Designer to choose colors to be used in the design.

Requirements
Must have
• A contact form and branding a product

```html
<!DOCTYPE html>
<html lang="en">
<head>
<meta charset="utf-8">
<title>Numeris Partners – Data Science &amp; Digital Marketing</title>
<link href="https://fonts.googleapis.com/css2?family=Lato:wght@400;700;900&family=Open+Sans:wght@400;600;700&display=swap" rel="stylesheet">
<style>
:root{
  --orange:#f15a24;
  --orange-deep:#d94a17;
  --ink:#222222;
  --text:#444444;
  --muted:#666666;
  --white:#ffffff;
  --panel:#f0f0f0;
  --footer:#262626;
  --line:#8a8a8a;
  --hero-dark:#06153a;
  --hero-mid:#0c3c8a;
  --hero-glow:#2f8fe0;
}
*{margin:0;padding:0;box-sizing:border-box}
html,body{width:1200px;height:3175px;overflow:hidden}
body{position:relative;background:var(--white);font-family:"Open Sans",Arial,sans-serif;color:var(--text)}
.abs{position:absolute}
.heading{font-family:"Lato",Arial,sans-serif}

/* header */
.site-header{left:0;top:0;width:1200px;height:116px;background:var(--white)}
.brand{display:flex;align-items:center;gap:12px;color:var(--orange);font-family:"Lato",Arial,sans-serif;font-weight:400;line-height:1}
.brand-dot{width:40px;height:40px;border-radius:50%;background:var(--orange);flex:none}
.brand-name{display:flex;flex-direction:column}
.brand-top{font-size:38px;letter-spacing:1px}
.brand-bottom{font-size:17px;letter-spacing:5.5px;margin-top:2px}
.site-header .brand{left:100px;top:30px}
.main-nav{left:442px;top:0;height:116px;display:flex;align-items:center;font-family:"Lato",Arial,sans-serif;font-size:17px;font-weight:700;color:var(--ink);letter-spacing:.5px}
.main-nav a{color:inherit;text-decoration:none;height:116px;display:flex;align-items:center;padding:0 22px}
.main-nav a.active{background:var(--orange);color:var(--white);padding:0 24px}

/* hero */
.hero{left:0;top:116px;width:1200px;height:515px;background:linear-gradient(100deg,var(--hero-dark) 0%,#0a2457 40%,var(--hero-mid) 70%,#0b2a66 100%)}
.hero-visual{right:0;top:0;width:520px;height:515px;background:radial-gradient(ellipse at 55% 45%,rgba(120,200,255,.75) 0%,var(--hero-glow) 25%,rgba(12,60,138,.4) 60%,rgba(6,21,58,0) 85%)}
.hero-title{left:100px;top:226px;font-family:"Lato",Arial,sans-serif;font-weight:900;font-size:46px;color:var(--white);letter-spacing:.5px}
.hero-text{left:100px;top:310px;font-size:15px;font-weight:600;line-height:23px;color:var(--white)}
.btn-outline{left:100px;top:396px;width:114px;height:51px;border:2px solid var(--white);color:var(--white);font-family:"Lato",Arial,sans-serif;font-weight:700;font-size:15px;display:flex;align-items:center;justify-content:center}
.slider-dots{left:100px;top:492px;display:flex;gap:6px}
.slider-dots span{width:16px;height:16px;border-radius:50%;background:rgba(255,255,255,.45)}
.slider-dots span.on{background:var(--white)}

/* services */
.section-title{width:1200px;left:0;text-align:center;font-family:"Lato",Arial,sans-serif;font-weight:700;font-size:26px;color:var(--orange);letter-spacing:.5px}
.services-title{top:686px}
.services-intro{left:150px;width:900px;top:740px;text-align:center;font-size:13.5px;line-height:28px;color:var(--text)}
.service{width:200px;text-align:center}
.service svg{display:block;margin:0 auto}
.service-name{font-family:"Lato",Arial,sans-serif;font-size:18px;color:var(--ink);margin-top:34px}
.service-name.highlight{color:var(--orange)}
.service-desc{font-size:12.5px;line-height:19px;color:var(--muted);margin-top:16px;padding:0 14px}

/* feature panels */
.feature{top:1212px;width:400px;height:354px;color:var(--white);text-align:center}
.feature-photo{position:absolute;inset:0}
.feature-1 .feature-photo{background:linear-gradient(135deg,#4a4640,#2e2c2a 60%,#3b3630)}
.feature-2 .feature-photo{background:linear-gradient(135deg,#b5440f,#8f3a12 60%,#a4461a)}
.feature-3 .feature-photo{background:linear-gradient(135deg,#2b2b2b,#1e1e1e 60%,#333)}
.feature-body{position:relative;padding-top:64px}
.feature-num{width:76px;height:76px;border:3px solid var(--white);border-radius:50%;margin:0 auto;display:flex;align-items:center;justify-content:center;font-family:"Lato",Arial,sans-serif;font-size:40px}
.feature-title{font-family:"Lato",Arial,sans-serif;font-weight:700;font-size:20px;margin-top:34px}
.feature-desc{font-size:13.5px;line-height:22px;margin:18px auto 0;width:300px}

/* product accordion */
.product-visual{left:116px;top:1646px;width:360px;height:318px;border-radius:8px;background:linear-gradient(160deg,#e9e9e9 0%,#cfcfcf 55%,#f4f4f4 100%)}
.accordion{left:578px;width:410px}
.acc-item{height:54px;border:2px solid var(--ink);border-radius:27px;display:flex;align-items:center;font-family:"Lato",Arial,sans-serif;font-size:16px;color:var(--ink)}
.acc-item .acc-icon{width:54px;height:54px;border-radius:50%;background:var(--ink);margin-left:-2px;display:flex;align-items:center;justify-content:center;flex:none}
.acc-item .acc-label{margin-left:16px}
.acc-item.open{border-color:var(--orange);color:var(--orange)}
.acc-item.open .acc-icon{background:var(--orange)}
.acc-text{font-size:13.5px;line-height:21px;color:var(--text);text-align:justify;padding:0 0 0 12px}

/* contact */
.contact{left:0;top:2070px;width:1200px;height:651px;background:var(--panel)}
.contact-title{top:2128px}
.title-rule{left:560px;top:2182px;width:80px;height:2px;background:var(--orange)}
.field{height:46px;border:2px solid var(--line);background:var(--panel);font-size:15px;color:var(--text);padding:0 0 0 34px;display:flex;align-items:center}
.field-icon{width:50px;height:50px;border-radius:50%;background:var(--orange);display:flex;align-items:center;justify-content:center}
.field-area{align-items:flex-start;padding-top:14px;height:176px}
.btn-send{left:527px;top:2600px;width:146px;height:49px;background:var(--orange);color:var(--white);font-family:"Lato",Arial,sans-serif;font-weight:700;font-size:15px;display:flex;align-items:center;justify-content:center;letter-spacing:.5px}

/* footer */
.site-footer{left:0;top:2721px;width:1200px;height:454px;background:var(--footer);color:var(--white)}
.footer-brand{left:100px;top:2850px;flex-direction:column;gap:14px;color:var(--white)}
.footer-brand .brand-dot{background:var(--white);width:50px;height:50px}
.footer-brand .brand-name{align-items:center}
.footer-brand .brand-top{font-size:42px;letter-spacing:2px}
.footer-brand .brand-bottom{font-size:18px;letter-spacing:6px}
.footer-head{font-family:"Lato",Arial,sans-serif;font-size:16px;font-weight:700;letter-spacing:.5px}
.footer-head::after{content:"";display:block;width:96px;height:2px;background:var(--white);margin-top:12px}
.links{list-style:none;font-size:14px;line-height:31px;margin-top:16px}
.links li::before{content:"> ";}
.contact-row{display:flex;gap:20px;margin-top:24px}
.round-icon{width:36px;height:36px;border:2px solid var(--white);border-radius:50%;flex:none;display:flex;align-items:center;justify-content:center}
.contact-row strong{display:block;font-size:14px;font-weight:700}
.contact-row span{font-size:12.5px;line-height:19px;display:block;margin-top:2px}
.social{display:flex;align-items:center;gap:16px;margin-top:20px;font-size:14px;font-weight:700;letter-spacing:.5px}
.social-dot{width:36px;height:36px;border:2px solid var(--white);border-radius:50%;flex:none}
.footer-rule{left:100px;top:3096px;width:1000px;height:1px;background:#555}
.copyright{left:0;width:1200px;top:3126px;text-align:center;font-size:14px;font-weight:600}
</style>
</head>
<body>

<header class="site-header abs">
  <div class="brand abs">
    <span class="brand-dot"></span>
    <span class="brand-name"><span class="brand-top">NUMERIS</span><span class="brand-bottom">PARTNERS</span></span>
  </div>
  <nav class="main-nav abs">
    <a class="active">HOME</a><a>ABOUT US</a><a>SERVICES</a><a>BLOG</a><a>NEWS</a><a>CONTACT US</a>
  </nav>
</header>

<section class="hero abs">
  <div class="hero-visual abs" role="img" aria-label="Glowing digital human head profile surrounded by lines of code and network connections"></div>
</section>
<h1 class="hero-title abs">NUMERIS PARTNERS</h1>
<p class="hero-text abs">Numeris Partners combines digital marketing with data science.<br>Target your customers at the right moment.</p>
<div class="btn-outline abs">Read More</div>
<div class="slider-dots abs"><span class="on"></span><span></span><span></span><span></span><span></span></div>

<h2 class="section-title services-title abs">OUR SERVICES</h2>
<p class="services-intro abs">Numeris Partners combines digital marketing with data science. Target your customers at the right moment, with the right message, through the right channel.</p>

<div class="service abs" style="left:84px;top:858px">
  <svg width="146" height="160" viewBox="0 0 146 160"><path d="M73 4a69 69 0 1 1-12 137l12 16 12-16A69 69 0 0 1 73 4z" transform="translate(0,-1)" fill="#fff" stroke="#222" stroke-width="2.5"/><path d="M50 84l30-30 12 34zM54 86l6 14 10-4-4-10M92 60l10-8M96 72l12 2M88 50l4-12" fill="#111" stroke="#111" stroke-width="3" stroke-linejoin="round"/></svg>
  <div class="service-name">Advisory</div>
  <p class="service-desc">We help our clients to identify their potential customers with the help of data science.</p>
</div>
<div class="service abs" style="left:291px;top:858px">
  <svg width="146" height="160" viewBox="0 0 146 160"><path d="M73 4a69 69 0 1 1-12 137l12 16 12-16A69 69 0 0 1 73 4z" fill="#f15a24"/><circle cx="73" cy="72" r="13" fill="none" stroke="#fff" stroke-width="3"/><path d="M66 90h14M68 96h10M73 46v8M52 72h-8M94 72h8M58 57l-6-6M88 57l6-6M56 66h34" stroke="#fff" stroke-width="3" stroke-linecap="round"/></svg>
  <div class="service-name highlight">Insights</div>
  <p class="service-desc">We help our clients to identify their potential customers with the help of data science.</p>
</div>
<div class="service abs" style="left:499px;top:858px">
  <svg width="146" height="160" viewBox="0 0 146 160"><path d="M73 4a69 69 0 1 1-12 137l12 16 12-16A69 69 0 0 1 73 4z" fill="#fff" stroke="#222" stroke-width="2.5"/><circle cx="73" cy="74" r="20" fill="none" stroke="#111" stroke-width="4"/><circle cx="73" cy="74" r="10" fill="none" stroke="#111" stroke-width="4"/><circle cx="73" cy="74" r="3" fill="#111"/><path d="M75 72l18-18M88 52h7v7" stroke="#111" stroke-width="4" fill="none"/></svg>
  <div class="service-name">Targeting &amp; optimization</div>
  <p class="service-desc">We help our clients to identify their potential customers with the help of data science.</p>
</div>
<div class="service abs" style="left:706px;top:858px">
  <svg width="146" height="160" viewBox="0 0 146 160"><path d="M73 4a69 69 0 1 1-12 137l12 16 12-16A69 69 0 0 1 73 4z" fill="#fff" stroke="#222" stroke-width="2.5"/><rect x="50" y="50" width="40" height="10" rx="2" fill="#111"/><rect x="50" y="64" width="40" height="10" rx="2" fill="#111"/><rect x="50" y="78" width="32" height="10" rx="2" fill="#111"/><circle cx="90" cy="86" r="8" fill="none" stroke="#111" stroke-width="3"/><path d="M70 88v12M54 100h32" stroke="#111" stroke-width="3"/></svg>
  <div class="service-name">Data engineering</div>
  <p class="service-desc">We help our clients to identify their potential customers with the help of data science.</p>
</div>
<div class="service abs" style="left:911px;top:858px">
  <svg width="146" height="160" viewBox="0 0 146 160"><path d="M73 4a69 69 0 1 1-12 137l12 16 12-16A69 69 0 0 1 73 4z" fill="#fff" stroke="#222" stroke-width="2.5"/><path d="M52 78a10 10 0 0 1 2-20 14 14 0 0 1 27-4 11 11 0 0 1 12 14 7 7 0 0 1-2 10z" fill="#111"/><rect x="62" y="74" width="22" height="18" rx="2" fill="#111" stroke="#fff" stroke-width="2"/><path d="M66 74v-5a7 7 0 0 1 14 0v5" fill="none" stroke="#fff" stroke-width="2"/></svg>
  <div class="service-name">Data privacy &amp; security</div>
  <p class="service-desc">We help our clients to identify their potential customers with the help of data science.</p>
</div>

<div class="feature feature-1 abs" style="left:0">
  <div class="feature-photo" role="img" aria-label="Dim desk scene with printed charts and a laptop showing analytics"></div>
  <div class="feature-body"><div class="feature-num">1</div><h3 class="feature-title">Predictive Analytics</h3><p class="feature-desc">This is our on-demand, software-as-a-service to capture, learn and target our client's website visitors.</p></div>
</div>
<div class="feature feature-2 abs" style="left:400px">
  <div class="feature-photo" role="img" aria-label="Orange-tinted photo of a team working with papers and laptops"></div>
  <div class="feature-body"><div class="feature-num">2</div><h3 class="feature-title">Conversion Modelling</h3><p class="feature-desc">This is our on-demand, software-as-a-service to capture, learn and target our client's website visitors.</p></div>
</div>
<div class="feature feature-3 abs" style="left:800px">
  <div class="feature-photo" role="img" aria-label="Dark photo of hands typing on a laptop keyboard"></div>
  <div class="feature-body"><div class="feature-num">3</div><h3 class="feature-title">Marketing Automation</h3><p class="feature-desc">This is our on-demand, software-as-a-service to capture, learn and target our client's website visitors.</p></div>
</div>

<div class="product-visual abs" role="img" aria-label="Desktop monitor, tablet and phone displaying the Lumoria product dashboard"></div>

<div class="accordion abs" style="top:1651px">
  <div class="acc-item open"><span class="acc-icon"><svg width="18" height="12" viewBox="0 0 18 12"><path d="M2 2l7 7 7-7" fill="none" stroke="#fff" stroke-width="3"/></svg></span><span class="acc-label">Digital Marketing</span></div>
</div>
<p class="accordion acc-text abs" style="top:1728px">Numeris Partners combines digital marketing with data science. Target your customers at the right moment, with the right message, through the right channel. Numeris Partners combines digital marketing with data science. Target your customers at the right moment.</p>
<div class="accordion abs" style="top:1839px">
  <div class="acc-item"><span class="acc-icon"><svg width="18" height="12" viewBox="0 0 18 12"><path d="M2 2l7 7 7-7" fill="none" stroke="#fff" stroke-width="3"/></svg></span><span class="acc-label">Profiling &amp; Targeting</span></div>
</div>
<div class="accordion abs" style="top:1923px">
  <div class="acc-item"><span class="acc-icon"><svg width="18" height="12" viewBox="0 0 18 12"><path d="M2 2l7 7 7-7" fill="none" stroke="#fff" stroke-width="3"/></svg></span><span class="acc-label">Data Management</span></div>
</div>

<section class="contact abs"></section>
<h2 class="section-title contact-title abs">CONTACT FORM</h2>
<div class="title-rule abs"></div>

<div class="field abs" style="left:154px;top:2277px;width:426px">Name</div>
<div class="field-icon abs" style="left:124px;top:2275px"><svg width="22" height="22" viewBox="0 0 22 22"><circle cx="11" cy="7" r="5" fill="#fff"/><path d="M2 21a9 8 0 0 1 18 0z" fill="#fff"/></svg></div>
<div class="field abs" style="left:645px;top:2277px;width:432px">Email Address</div>
<div class="field-icon abs" style="left:618px;top:2275px"><svg width="22" height="22" viewBox="0 0 22 22"><circle cx="11" cy="7" r="5" fill="#fff"/><path d="M2 21a9 8 0 0 1 18 0z" fill="#fff"/></svg></div>
<div class="field field-area abs" style="left:154px;top:2378px;width:923px">Write something for us</div>
<div class="field-icon abs" style="left:124px;top:2355px"><svg width="22" height="22" viewBox="0 0 22 22"><circle cx="11" cy="7" r="5" fill="#fff"/><path d="M2 21a9 8 0 0 1 18 0z" fill="#fff"/></svg></div>
<div class="btn-send abs">SEND MESSAGE</div>

<footer class="site-footer abs"></footer>
<div class="brand footer-brand abs">
  <span class="brand-dot"></span>
  <span class="brand-name"><span class="brand-top">NUMERIS</span><span class="brand-bottom">PARTNERS</span></span>
</div>

<div class="abs" style="left:385px;top:2806px;color:#fff">
  <div class="footer-head">USEFULL LINKS</div>
  <ul class="links"><li>Home</li><li>About Us</li><li>Services</li><li>Blog</li><li>News</li><li>Contact Us</li></ul>
</div>

<div class="abs" style="left:614px;top:2806px;color:#fff;width:240px">
  <div class="footer-head">CONTACT US</div>
  <div class="contact-row"><span class="round-icon"><svg width="12" height="16" viewBox="0 0 12 16"><path d="M6 15C2 10 1 8 1 6a5 5 0 0 1 10 0c0 2-1 4-5 9z" fill="#fff"/><circle cx="6" cy="6" r="2" fill="#262626"/></svg></span><div><strong>ADDRESS,</strong><span>48 Willowgracht, Veldhaven,<br>The Netherlands.</span></div></div>
  <div class="contact-row"><span class="round-icon"><svg width="10" height="16" viewBox="0 0 10 16"><rect x="1" y="1" width="8" height="14" rx="1.5" fill="none" stroke="#fff" stroke-width="1.8"/></svg></span><div><strong>PHONE NUMBER:</strong><span>+31 (0)6 20583147</span></div></div>
  <div class="contact-row"><span class="round-icon"><svg width="16" height="12" viewBox="0 0 16 12"><rect x="1" y="1" width="14" height="10" fill="#fff"/><path d="M1 1l7 6 7-6" fill="none" stroke="#262626" stroke-width="1.5"/></svg></span><div><strong>EMAIL:</strong><span>hello@numerispartners.com</span></div></div>
</div>

<div class="abs" style="left:952px;top:2804px;color:#fff">
  <div class="footer-head">CONTACT FORM</div>
  <div class="social"><span class="social-dot"></span>KINDRED</div>
  <div class="social"><span class="social-dot"></span>CHIRPER</div>
  <div class="social"><span class="social-dot"></span>SNAPFRAME</div>
  <div class="social"><span class="social-dot"></span>PROLINK</div>
</div>

<div class="footer-rule abs"></div>
<p class="copyright abs" style="color:#fff">Copyrights @ 2017 Numeris Partners. All Rights Reserved.</p>

</body>
</html>
```